Business card for Eyelash extension salon in Beverly Hills,California USA

We need new business card for our salon in Beverly Hills. The salon name is 'Lumarra' . We would like to have...Business name: Lumarra Name of person: will provide later Address 6128 N.Corbel Ridge Blvd Westmere Vale , CA 90417 Phone: will provide later (Text only) Web: www.lumarrastudio-example.com Pictogrid icon, Friendvale icon follow us for seasonal campaign and news @lumarrastudioexample Design should look elegant, high-end, clean, simple, cohesive with my brand. Please refer my brand board. Business name color will be metallic bronzy color. Im thinking grey background or white background. Thanks

Target Market(s)

25-35. Gender neutral. People who are in Entertainment business industry.
This is High-end Eyelash extension salon in Beverly Hills

Industry/Entity Type

Beauty Salon

Contact Information for Business Card

Business name: Lumarra
Name of person: will provide later
Address 6128 N.Corbel Ridge Blvd Westmere Vale , CA 90417
Phone: will provide later (Text only)
Web: www.lumarrastudio-example.com
Pictogrid icon, Friendvale icon
follow us for seasonal campaign and news @lumarrastudioexample

Requirements
Must have
• Beautiful, elegant, clean and simple look but very attractive and modern
Should not have
• We don't like too clutter, too busy designs.

```html
<!DOCTYPE html>
<html lang="en">
<head>
<meta charset="utf-8">
<title>Lumarra Business Card</title>
<link rel="stylesheet" href="https://fonts.googleapis.com/css2?family=Tinos&display=swap">
<style>
  :root {
    --ink: #000000;
    --paper: #ffffff;
    --bronze: #c8943a;
    --pattern-light: #f4f4f4;
    --pattern-mid: #dcdcdc;
  }
  * { margin: 0; padding: 0; box-sizing: border-box; }
  html, body {
    width: 1200px;
    height: 1200px;
    overflow: hidden;
    background: var(--paper);
  }
  body {
    position: relative;
    font-family: "Tinos", "Times New Roman", serif;
    color: var(--ink);
  }
  .card {
    position: absolute;
    border: 10px solid var(--ink);
    background: var(--paper);
    overflow: hidden;
  }
  .card-front { left: 118px; top: 62px; width: 974px; height: 496px; }
  .card-back  { left: 123px; top: 620px; width: 975px; height: 490px; }

  .lash-pattern {
    position: absolute;
    inset: 0;
    background: radial-gradient(circle at 50% 50%, var(--pattern-light) 0%, var(--pattern-mid) 100%);
  }
  .brand-panel {
    position: absolute;
    left: 212px;
    top: 70px;
    width: 530px;
    height: 326px;
    background: var(--ink);
    display: flex;
    align-items: center;
    justify-content: center;
  }
  .brand-name {
    font-family: "Tinos", "Times New Roman", serif;
    font-weight: 400;
    color: var(--bronze);
    letter-spacing: 2px;
  }
  .brand-panel .brand-name { font-size: 104px; }

  .card-back .brand-name {
    position: absolute;
    left: 44px;
    top: 56px;
    font-size: 60px;
    line-height: 1;
  }
  .contact {
    position: absolute;
    left: 473px;
    top: 132px;
  }
  .contact-name { font-size: 53px; line-height: 56px; }
  .contact-line { font-size: 31.5px; line-height: 39px; white-space: nowrap; }
  .contact-address { margin-top: 38px; }
  .social {
    position: absolute;
    left: 473px;
    top: 416px;
    display: flex;
    gap: 16px;
    align-items: center;
    font-size: 17px;
  }
  .social-item { display: flex; align-items: center; gap: 6px; }
  .social-square { width: 22px; height: 22px; background: var(--ink); }
  .social-circle { width: 22px; height: 22px; border: 2px solid var(--ink); border-radius: 50%; }
  .follow-note {
    position: absolute;
    left: 473px;
    top: 446px;
    font-size: 17.5px;
    line-height: 20px;
    white-space: nowrap;
  }
</style>
</head>
<body>
  <section class="card card-front">
    <div class="lash-pattern" role="img" aria-label="Repeating pattern of black closed eyelashes on white"></div>
    <div class="brand-panel">
      <span class="brand-name">Lumarra</span>
    </div>
  </section>

  <section class="card card-back">
    <span class="brand-name">Lumarra</span>
    <div class="contact">
      <p class="contact-name">Name</p>
      <p class="contact-line">www.lumarrastudio-example.com</p>
      <p class="contact-line">Phone no.</p>
      <div class="contact-address">
        <p class="contact-line">6128 N.Corbel Ridge Blvd</p>
        <p class="contact-line">Westmere Vale , CA 90417</p>
      </div>
    </div>
    <div class="social">
      <span class="social-item"><span class="social-square"></span>Friendvale</span>
      <span class="social-item"><span class="social-circle"></span>Pictogrid</span>
    </div>
    <p class="follow-note">follow us for seasonal campaign and news @lumarrastudioexample</p>
  </section>
</body>
</html>
```